Business card design for Velvet Harbor

We need business cards designed for our new marketing consulting company, Velvet Harbor. Our services include marketing strategy, go-to-market and launch planning, growth strategy, and execution. We serve medical technology and health technology companies, from startups to well-established growth companies.

The business cards should feel professional, credible, reliable and trustworthy, and should instill confidence. Also bold, creative, and modern.

The design must use the Velvet Harbor logo.

The primary brand color is this orange: #FF5501
A secondary color that you can use is this gray: #282B2D
I would prefer only to use the orange and gray. But if you feel you really need an additional accent color (please use it very sparingly, as little as possible), you can use this blue for small accent purposes: #009FED

Attached are the logo files. The main logo is the one with a little bit of orange on the left and the rest is gray.

The business card should include the following:

Velvet Harbor logo
First name and last name
Title
Email address
Phone number and type (in whatever order looks best for the design
Website (the website does not need to be in the same block as the personal info)

For example:

Nessa Pryle
Founder & Principal
nessa@velvetharbor.com
+1.628.309.4156 mobile (can use "." or spaces in between blocks of numbers)
velvetharbor.com (somewhere on the card, it does not need to be with the personal info; and note that there is no "www." at the beginning)

Note that there will be no address listed on the business card.

Target Market(s)

Executives (CEO, head of marketing, head of sales) at medical technology and health technology companies, mostly in their 40s and older, well-educated, often with advanced degrees. They are strategic thinkers, responsible for budgets, and familiar with P&L. Their comfort with and trust in using outside consultants varies.

Industry/Entity Type

Medical technology and health technology companies.

Contact Information for Business Card

See project description

Font styles to use
Sans Serif

Requirements
Must have
• Logo and see Business card details section above.

```html
<!DOCTYPE html>
<html lang="en">
<head>
<meta charset="utf-8">
<title>Velvet Harbor — Business Card</title>
<link rel="stylesheet" href="https://fonts.googleapis.com/css2?family=Arimo:wght@400;500;700&display=swap">
<style>
  :root {
    --orange: #FF5501;
    --charcoal: #282B2D;
    --shadow-grey: #AFB2B5;
    --paper: #FFFFFF;
  }
  * { margin: 0; padding: 0; box-sizing: border-box; }
  html, body {
    width: 944px;
    height: 1200px;
    overflow: hidden;
    background: var(--paper);
    font-family: "Arimo", Arial, sans-serif;
  }
  .canvas { position: relative; width: 944px; height: 1200px; }

  .card-shadow { position: absolute; background: var(--shadow-grey); }
  .card { position: absolute; width: 905px; height: 517px; overflow: hidden; }

  /* front */
  .front-shadow { left: 38px; top: 38px; width: 906px; height: 516px; }
  .card-front { left: 0; top: 0; background: var(--paper); }
  .edge-bar { position: absolute; background: var(--orange); width: 17px; height: 218px; }
  .card-front .edge-bar { left: 0; top: 150px; border-radius: 0 9px 9px 0; }

  .wordmark {
    position: absolute;
    display: flex;
    align-items: center;
    gap: 14px;
  }
  .wordmark-dot { border-radius: 50%; background: var(--orange); flex: none; }
  .wordmark-name {
    font-weight: 700;
    text-transform: uppercase;
    line-height: 1.02;
  }
  .card-front .wordmark { left: 140px; top: 233px; }
  .card-front .wordmark-dot { width: 14px; height: 14px; }
  .card-front .wordmark-name { color: var(--charcoal); font-size: 21px; letter-spacing: 5px; }

  .divider { position: absolute; left: 471px; top: 125px; width: 5px; height: 269px; background: var(--orange); }

  .contact-list { position: absolute; left: 524px; top: 168px; list-style: none; }
  .contact-item { display: flex; align-items: center; height: 40px; margin-bottom: 32px; }
  .contact-icon {
    width: 40px; height: 40px; border-radius: 4px;
    background: var(--orange);
    display: flex; align-items: center; justify-content: center;
    flex: none;
  }
  .contact-text { margin-left: 16px; color: var(--charcoal); }
  .person-name { font-size: 19px; font-weight: 500; line-height: 20px; text-transform: uppercase; }
  .person-title { font-size: 19px; font-weight: 500; line-height: 20px; }
  .contact-value { font-size: 23px; }

  /* back */
  .back-shadow { left: 38px; top: 683px; width: 906px; height: 517px; }
  .card-back { left: 0; top: 649px; background: var(--charcoal); }
  .card-back .edge-bar { right: 0; top: 145px; border-radius: 9px 0 0 9px; }
  .card-back .wordmark { left: 262px; top: 210px; gap: 34px; }
  .card-back .wordmark-dot { width: 30px; height: 30px; }
  .card-back .wordmark-name { color: var(--paper); font-size: 42px; letter-spacing: 12px; line-height: 1.05; }
</style>
</head>
<body>
<main class="canvas">

  <div class="card-shadow front-shadow"></div>
  <section class="card card-front" aria-label="Business card front">
    <div class="edge-bar"></div>

    <div class="wordmark">
      <span class="wordmark-dot"></span>
      <span class="wordmark-name">Velvet<br>Harbor</span>
    </div>

    <div class="divider"></div>

    <ul class="contact-list">
      <li class="contact-item">
        <span class="contact-icon">
          <svg width="26" height="28" viewBox="0 0 26 28" aria-hidden="true">
            <circle cx="13" cy="7" r="6" fill="#fff"/>
            <path d="M2 27 V19 Q2 14 7 14 H19 Q24 14 24 19 V27 Z" fill="#fff"/>
            <rect x="12" y="14" width="2" height="13" fill="#FF5501"/>
          </svg>
        </span>
        <div class="contact-text">
          <div class="person-name">Nessa Pryle</div>
          <div class="person-title">Founder &amp; Principal</div>
        </div>
      </li>
      <li class="contact-item">
        <span class="contact-icon">
          <svg width="28" height="22" viewBox="0 0 28 22" aria-hidden="true">
            <path d="M1 8 L14 1 L27 8 V21 H1 Z" fill="#fff"/>
            <path d="M1 8 L14 16 L27 8" fill="none" stroke="#FF5501" stroke-width="1.6"/>
            <rect x="9" y="6" width="10" height="1.6" fill="#FF5501"/>
            <rect x="9" y="9" width="10" height="1.6" fill="#FF5501"/>
          </svg>
        </span>
        <span class="contact-text contact-value">nessa@velvetharbor.com</span>
      </li>
      <li class="contact-item">
        <span class="contact-icon">
          <svg width="24" height="24" viewBox="0 0 24 24" aria-hidden="true">
            <path d="M17 2 L21 6 L18 9 L15 7 Q10 11 7 15 L9 18 L6 21 L2 17 Q3 7 17 2 Z" fill="#fff"/>
          </svg>
        </span>
        <span class="contact-text contact-value">+1.628.309.4156</span>
      </li>
    </ul>
  </section>

  <div class="card-shadow back-shadow"></div>
  <section class="card card-back" aria-label="Business card back">
    <div class="edge-bar"></div>
    <div class="wordmark">
      <span class="wordmark-dot"></span>
      <span class="wordmark-name">Velvet<br>Harbor</span>
    </div>
  </section>

</main>
</body>
</html>
```